PowerPoint Re-Design and Template Needs a Designer's Eye!

I have the text, images and logo for a PowerPoint but need your Design and Template skills! Less than 20 pages, needs to be concise, include images, must have creative page layouts, include our floater-logo on every page, use sidebars or call-outs for important information, have color but not too much because this will be printed many times (our current colors are too dark). You can use bullet-points or paragraphs. You can also change the titles, font, color, layout - anything! This is YOUR PowerPoint to create the most impressive Template! We are an investment management firm located in New York City. Our investment returns are the very best in the industry and we want this PowerPoint to convey our "best in class" style.

Notes:
1) Please use the PPP outline attached.
2) I have attached a rough draft PPP. Please use the logos on page 2. Some pages do not have text, the final text will be available shortly.
3) I have attached examples you can reference.
4) Please include our floater-logo on every page.
5) Please feel free to ask questions or clarification.
Updates

Hi Designers, Thank you very much for your wonderful submissions! My partners and I are going through each submission in detail today and tomorrow. We'll be in touch over the next few days with additional questions and comments. Stay tuned! Best, Norman Pasquale

Target Market(s)

High-net worth individuals and institutions. New York City, Wall Street.

Industry/Entity Type

Investment

Requirements
Must have
• - Floater-logo on every page
- Sidebars or call-outs on several pages (you can decide which ones)
- Please include images; however, the PPP Template is the most important.

```html
<!DOCTYPE html>
<html lang="en">
<head>
<meta charset="utf-8">
<title>Our Philosophy</title>
<link rel="stylesheet" href="https://fonts.googleapis.com/css2?family=Archivo:wght@800&family=Questrial&family=Roboto+Condensed:wght@400&display=swap">
<style>
  :root {
    --brand-orange: #f47a00;
    --rule-grey: #b9b9b9;
    --footer-grey: #6a6a6a;
    --body-text: #4a4a4a;
    --title-ink: #111111;
    --paper: #ffffff;
  }
  html, body {
    margin: 0;
    padding: 0;
    width: 1200px;
    height: 900px;
    overflow: hidden;
    background: var(--paper);
  }
  .slide {
    position: relative;
    width: 1200px;
    height: 900px;
    background: var(--paper);
    overflow: hidden;
  }
  .slide-header {
    position: absolute;
    left: 0; top: 0;
    width: 1200px;
    height: 94px;
    background: var(--brand-orange);
    border-bottom: 3px solid var(--rule-grey);
  }
  .slide-title {
    position: absolute;
    left: 27px;
    top: 33px;
    margin: 0;
    font-family: "Archivo", Arial, sans-serif;
    font-weight: 800;
    font-size: 34px;
    line-height: 1;
    letter-spacing: 0.5px;
    color: var(--title-ink);
  }
  .firm-name {
    position: absolute;
    right: 26px;
    top: 35px;
    font-family: "Questrial", sans-serif;
    font-size: 22px;
    line-height: 1;
    color: var(--paper);
  }
  .philosophy-copy {
    position: absolute;
    left: 80px;
    top: 172px;
    width: 1090px;
    font-family: "Questrial", sans-serif;
    font-size: 23px;
    line-height: 39px;
    color: var(--body-text);
  }
  .philosophy-copy p {
    margin: 0 0 52px 0;
  }
  .slide-footer {
    position: absolute;
    left: 0; bottom: 0;
    width: 1200px;
    height: 40px;
    background: var(--footer-grey);
    font-family: "Roboto Condensed", Arial, sans-serif;
    font-size: 18px;
    color: var(--paper);
  }
  .footer-credit {
    position: absolute;
    left: 8px;
    top: 10px;
  }
  .footer-page {
    position: absolute;
    right: 12px;
    top: 10px;
  }
</style>
</head>
<body>
  <main class="slide">
    <header class="slide-header">
      <h1 class="slide-title">OUR PHILOSOPHY</h1>
      <div class="firm-name">Meridale Partners</div>
    </header>

    <section class="philosophy-copy">
      <p>We are long-term investors who buy deeply valued securities in companies we want to own. We are contrarian in nature and seek opportunities with strong cash flow, inexpensive assets and multiple competitive advantages.</p>
      <p>We are thematic at the macro-level and use a bottom-up, research-intensive evaluation process at the sector and security level. This process includes analyzing securities at the quantitative and qualitative levels.</p>
      <p>Risk is a significant focus that often keeps us inactive and sitting with cash. The securities we purchase are the ones remaining after risk-analysis.</p>
      <p>Our size per position varies for many reasons and is used as a form of risk management.</p>
    </section>

    <footer class="slide-footer">
      <span class="footer-credit">Norman Pasquale 2015</span>
      <span class="footer-page">Page : 01</span>
    </footer>
  </main>
</body>
</html>
```